Quorvex business card design

create modern and tech looking business card that is clean but effectively communciates that we are a cloud communications company.
Should have at minimum:
Employee Name
Postion
Phone Number
Email
website
create modern and tech looking business card that is clean but effectively communciates that we are a cloud communications company. We have two logo color schemes (attached) so would like to see designs both ways
Should have at minimum:
Employee Name
Postion
Phone Number
Email
website

```html
<!DOCTYPE html>
<html lang="en">
<head>
<meta charset="utf-8">
<title>Quorvex business card</title>
<link href="https://fonts.googleapis.com/css2?family=Open+Sans:wght@400;600;700&display=swap" rel="stylesheet">
<style>
  :root {
    --backdrop: #ecebe8;
    --sky: #2bbbe0;
    --paper: #f7f7f7;
    --violet: #5e2a96;
    --cyan: #2eb6df;
    --ink: #4a4a4a;
    --text: #2b2b2b;
  }
  * { margin: 0; padding: 0; box-sizing: border-box; }
  html, body {
    width: 1200px; height: 900px; overflow: hidden;
    background: var(--backdrop);
    font-family: "Open Sans", Arial, sans-serif;
  }
  .canvas { position: relative; width: 1200px; height: 900px; }
  .card {
    position: absolute;
    width: 640px; height: 366px;
    border-radius: 3px;
    box-shadow: 0 10px 24px rgba(0,0,0,.18);
    overflow: hidden;
  }
  .card--front { left: 120px; top: 140px; background: var(--sky); }
  .card--back { left: 440px; top: 380px; background: var(--paper); }

  .brand {
    position: absolute;
    display: flex; align-items: center; gap: 14px;
  }
  .brand__mark { width: 26px; height: 26px; background: var(--violet); }
  .brand__name {
    font-weight: 600; font-size: 46px; letter-spacing: 2px;
    color: var(--ink); line-height: 1;
  }
  .card--front .brand { left: 50%; top: 50%; transform: translate(-50%, -50%); }
  .card--back .brand { left: 70px; top: 70px; }

  .person { position: absolute; left: 70px; top: 196px; }
  .person__name {
    font-weight: 700; font-size: 21px; letter-spacing: .5px; line-height: 1.1;
  }
  .person__first { color: var(--violet); }
  .person__last { color: var(--cyan); }
  .person__role { font-size: 15px; color: var(--text); margin-top: 2px; }

  .contacts { position: absolute; left: 70px; top: 270px; list-style: none; }
  .contacts li {
    display: flex; align-items: center; gap: 10px;
    font-size: 16px; color: var(--text); line-height: 26px;
  }
  .contacts svg { width: 14px; height: 14px; fill: var(--violet); flex: none; }
</style>
</head>
<body>
<main class="canvas">
  <section class="card card--front" aria-label="Card front">
    <div class="brand">
      <span class="brand__mark"></span>
      <span class="brand__name">QUORVEX</span>
    </div>
  </section>

  <section class="card card--back" aria-label="Card back">
    <div class="brand">
      <span class="brand__mark"></span>
      <span class="brand__name">QUORVEX</span>
    </div>

    <div class="person">
      <p class="person__name"><span class="person__first">DANIEL</span> <span class="person__last">MARSH</span></p>
      <p class="person__role">Managing Director</p>
    </div>

    <ul class="contacts">
      <li>
        <svg viewBox="0 0 24 24" aria-hidden="true"><path d="M6.6 10.8a15.1 15.1 0 0 0 6.6 6.6l2.2-2.2a1 1 0 0 1 1-.25 11.4 11.4 0 0 0 3.6.57 1 1 0 0 1 1 1V20a1 1 0 0 1-1 1A17 17 0 0 1 3 4a1 1 0 0 1 1-1h3.5a1 1 0 0 1 1 1c0 1.25.2 2.45.57 3.57a1 1 0 0 1-.25 1z"/></svg>
        (044)987650321
      </li>
      <li>
        <svg viewBox="0 0 24 24" aria-hidden="true"><path d="M2 5h20v14H2z M3.5 6.5v.4L12 12.6l8.5-5.7v-.4z" fill-rule="evenodd"/></svg>
        info@quorvexmail.com
      </li>
      <li>
        <svg viewBox="0 0 24 24" aria-hidden="true"><circle cx="12" cy="12" r="10"/><path d="M2 12h20M12 2c3 3 3 17 0 20M12 2c-3 3-3 17 0 20" stroke="#f7f7f7" stroke-width="1.6" fill="none"/></svg>
        www.quorvexcloud.com
      </li>
    </ul>
  </section>
</main>
</body>
</html>
```